we are starting an online childrens clothing store, The Otter And The Kite, and require an easy to navigate, simple and elegant in design. we will suply our own domain and company logo.

Target Market(s)

Familys with children aged 0 to 8

Industry/Entity Type

Clothing

Requirements
Must have
• easy to navigate,
our company logo on the header of each page
easy two step checkout with coinrill access.
easy to modify and add to site by us at no or minimal cost.
6 pages, home page, boys clothing, girls clothing, our brands, about us, contact.
brightmark ads
kin wall link
Should not have
• pop up ads
dark colours

```html
<!DOCTYPE html>
<html lang="en">
<head>
<meta charset="utf-8">
<title>The Otter And The Kite — Children's Clothing</title>
<link rel="stylesheet" href="https://fonts.googleapis.com/css2?family=Oswald:wght@400;500&family=Lobster&family=Courgette&family=Arimo:wght@400&display=swap">
<style>
:root{
  --green:#7cb82f;
  --green-dark:#5f9a1c;
  --green-soft:#b9dc8f;
  --ink:#4a4a4a;
  --muted:#888;
  --line:#e3e3e3;
  --page:#eef3f9;
  --white:#ffffff;
  --title-blue:#1a2be0;
  --footer:#3b3b3b;
  --footer-text:#c9c9c9;
}
*{box-sizing:border-box;margin:0;padding:0}
html,body{width:706px;height:1200px;overflow:hidden}
body{background:var(--page);font-family:"Arimo",Arial,sans-serif;color:var(--ink);position:relative}
a{color:inherit;text-decoration:none}

/* Header */
.site-header{position:absolute;top:0;left:0;width:706px;height:56px;background:var(--white)}
.brand{position:absolute;left:24px;top:20px;font-family:"Oswald",sans-serif;font-weight:500;font-size:17px;color:var(--green);letter-spacing:.2px}
.social{position:absolute;right:18px;top:2px;display:flex;gap:8px;font-family:"Arimo",sans-serif;font-size:7px;color:#333}
.social a{display:flex;align-items:center;gap:2px}
.social a::before{content:"";width:5px;height:5px;background:#333;display:block}
.account-links{position:absolute;left:378px;top:20px;width:227px;height:24px;border:1px solid var(--line);display:flex;align-items:center;justify-content:center;gap:6px;font-size:7.5px;color:var(--muted)}
.account-links a+a::before{content:"";display:inline-block;width:4px;height:4px;background:var(--green);margin-right:6px;vertical-align:1px}
.mini-cart{position:absolute;left:608px;top:20px;width:78px;height:24px;background:var(--green);color:var(--white);font-size:7px;padding:2px 4px}
.mini-cart .label{display:block;text-align:center}
.mini-cart .count{display:flex;justify-content:space-between;align-items:center;margin-top:1px}

/* Navigation */
.main-nav{position:absolute;top:56px;left:0;width:706px;height:32px;background:var(--white);border-top:1px solid var(--line);border-bottom:1px solid var(--line);box-shadow:0 1px 2px rgba(0,0,0,.05)}
.main-nav ul{list-style:none;display:flex;position:absolute;left:31px;top:0;height:30px}
.main-nav li a{display:block;height:30px;line-height:30px;padding:0 7px;font-family:"Oswald",sans-serif;font-size:8.5px;color:#555;letter-spacing:.2px}
.main-nav li.active a{background:var(--green-soft);color:var(--white)}
.search{position:absolute;left:570px;top:9px;display:flex}
.search .field{width:80px;height:16px;border:1px solid var(--line);background:var(--white)}
.search .go{width:36px;height:16px;background:var(--green);color:var(--white);font-size:7px;display:flex;align-items:center;justify-content:center}

/* Hero */
.hero{position:absolute;left:11px;top:89px;width:695px;height:226px;background:linear-gradient(100deg,#efece9 0%,#d9b7c6 20%,#b9a1c0 40%,#e9e2e0 55%,#5fa8b0 72%,#8a6f8c 88%,#ece9e8 100%)}

/* Product sections */
.shelf{position:absolute;left:24px;width:664px;height:208px;background:var(--white);border:1px solid var(--line)}
.shelf-title{height:32px;border-bottom:1px solid var(--line);font-family:"Courgette",cursive;font-size:13px;color:var(--title-blue);padding:6px 0 0 7px;font-style:italic}
.shelf-grid{display:grid;grid-template-columns:152px 171px 176px 163px;height:174px}
.product{border-left:1px solid var(--line);display:flex;flex-direction:column;align-items:center}
.product:first-child{border-left:none}
.product-name{width:100%;height:22px;border-bottom:1px solid var(--line);font-family:"Oswald",sans-serif;font-size:7px;color:#555;display:flex;align-items:center;justify-content:center}
.product-photo{width:142px;height:113px;margin-top:7px}
.photo-shirt{background:linear-gradient(160deg,#ffffff 10%,#7f93e0 40%,#6a7fd6 70%,#ffffff 95%)}
.photo-white-dress{background:linear-gradient(150deg,#eceae8,#ffffff 50%,#d8d6d4)}
.photo-jacket{background:linear-gradient(90deg,#e8e8e8,#3c3b3e 20%,#8a8a8c 45%,#3a3a44 70%,#e8e8e8)}
.photo-orange-dress{background:radial-gradient(ellipse at 50% 70%,#f0643c 0%,#ec6a44 35%,#c9a490 70%,#b89a88 100%)}
.buy{margin-top:11px;width:142px;height:23px;background:var(--green);border-radius:2px;display:flex;align-items:center;color:var(--white);font-family:"Oswald",sans-serif}
.buy .price{width:60px;text-align:center;font-size:11px;border-right:1px solid var(--green-dark)}
.buy .add{flex:1;display:flex;align-items:center;justify-content:space-between;padding:0 7px;font-size:7.5px}

/* Footer */
.site-footer{position:absolute;left:0;top:1050px;width:706px;height:150px;background:var(--footer);color:var(--footer-text)}
.footer-cols{position:absolute;left:57px;top:27px;display:grid;grid-template-columns:170px 170px 169px 140px}
.footer-cols h3{font-family:"Lobster",cursive;font-weight:400;font-size:13px;color:var(--white);margin-bottom:5px}
.footer-cols ul{list-style:none}
.footer-cols li{font-size:6.5px;line-height:14px}
.footer-cols li::before{content:"›";margin-right:4px;color:#999}
.footer-bottom{position:absolute;left:36px;right:36px;top:125px;height:14px;border-top:1px solid #555}
.copyright{position:absolute;left:12px;top:3px;font-family:"Oswald",sans-serif;font-size:5px;color:var(--white);display:flex;gap:4px}
.copyright span+span{border-left:1px solid #aaa;padding-left:4px}
.pager{position:absolute;left:334px;top:-6px;display:flex;gap:5px;align-items:center}
.pager i{display:block;width:6px;height:6px;border-radius:50%;background:#999}
.pager i.on{width:10px;height:10px;background:#aaa}
</style>
</head>
<body>

<header class="site-header">
  <div class="brand">The Otter And The Kite</div>
  <nav class="social" aria-label="Social links">
    <a href="#">kin wall</a><a href="#">Chirpline</a><a href="#">Feed</a><a href="#">Circleplus</a>
  </nav>
  <nav class="account-links">
    <a href="#">My Account</a><a href="#">Wishlist</a><a href="#">My Cart</a><a href="#">CheckOut</a><a href="#">Log In</a>
  </nav>
  <div class="mini-cart">
    <span class="label">Shopping Cart</span>
    <span class="count">
      <svg width="14" height="10" viewBox="0 0 14 10" aria-hidden="true"><path d="M0 1h3l2 6h7l1-4H4" fill="none" stroke="#fff" stroke-width="1.3"/><circle cx="6" cy="9" r="1" fill="#fff"/><circle cx="11" cy="9" r="1" fill="#fff"/></svg>
      <span>0 item-$0.00</span>
    </span>
  </div>
</header>

<nav class="main-nav">
  <ul>
    <li class="active"><a href="#">HOME</a></li>
    <li><a href="#">BOYS CLOTHING</a></li>
    <li><a href="#">GIRLS CLOTHING</a></li>
    <li><a href="#">OUR BRANDS</a></li>
    <li><a href="#">ABOUT US</a></li>
    <li><a href="#">CONTACT</a></li>
    <li><a href="#">BRIGHTMARK ADS</a></li>
  </ul>
  <div class="search"><span class="field"></span><span class="go">Search</span></div>
</nav>

<div class="hero" role="img" aria-label="Group of smiling children in colourful winter outfits walking hand in hand"></div>

<section class="shelf" style="top:337px">
  <h2 class="shelf-title">New Arrivals</h2>
  <div class="shelf-grid">
    <article class="product"><div class="product-name">NON IRON SHIRT FOR BOYS</div><div class="product-photo photo-shirt" role="img" aria-label="Blue short-sleeve boys shirt"></div><div class="buy"><span class="price">$50</span><span class="add">ADD TO CART<svg width="16" height="12" viewBox="0 0 14 10" aria-hidden="true"><path d="M0 1h3l2 6h7l1-4H4" fill="none" stroke="#222" stroke-width="1.3"/><circle cx="6" cy="9" r="1" fill="#222"/><circle cx="11" cy="9" r="1" fill="#222"/></svg></span></div></article>
    <article class="product"><div class="product-name">GIRLS FANCY DRESS</div><div class="product-photo photo-white-dress" role="img" aria-label="Girl in a white layered party dress"></div><div class="buy"><span class="price">$50</span><span class="add">ADD TO CART<svg width="16" height="12" viewBox="0 0 14 10" aria-hidden="true"><path d="M0 1h3l2 6h7l1-4H4" fill="none" stroke="#222" stroke-width="1.3"/><circle cx="6" cy="9" r="1" fill="#222"/><circle cx="11" cy="9" r="1" fill="#222"/></svg></span></div></article>
    <article class="product"><div class="product-name">BOYS JACKET</div><div class="product-photo photo-jacket" role="img" aria-label="Four boys wearing jackets and jeans"></div><div class="buy"><span class="price">$50</span><span class="add">ADD TO CART<svg width="16" height="12" viewBox="0 0 14 10" aria-hidden="true"><path d="M0 1h3l2 6h7l1-4H4" fill="none" stroke="#222" stroke-width="1.3"/><circle cx="6" cy="9" r="1" fill="#222"/><circle cx="11" cy="9" r="1" fill="#222"/></svg></span></div></article>
    <article class="product"><div class="product-name">GIRLS FANCY DRESS</div><div class="product-photo photo-orange-dress" role="img" aria-label="Girl in an orange ruffled dress"></div><div class="buy"><span class="price">$50</span><span class="add">ADD TO CART<svg width="16" height="12" viewBox="0 0 14 10" aria-hidden="true"><path d="M0 1h3l2 6h7l1-4H4" fill="none" stroke="#222" stroke-width="1.3"/><circle cx="6" cy="9" r="1" fill="#222"/><circle cx="11" cy="9" r="1" fill="#222"/></svg></span></div></article>
  </div>
</section>

<section class="shelf" style="top:566px">
  <h2 class="shelf-title">Girls Dresses</h2>
  <div class="shelf-grid">
    <article class="product"><div class="product-name">NON IRON SHIRT FOR BOYS</div><div class="product-photo photo-shirt" role="img" aria-label="Blue short-sleeve boys shirt"></div><div class="buy"><span class="price">$50</span><span class="add">ADD TO CART<svg width="16" height="12" viewBox="0 0 14 10" aria-hidden="true"><path d="M0 1h3l2 6h7l1-4H4" fill="none" stroke="#222" stroke-width="1.3"/><circle cx="6" cy="9" r="1" fill="#222"/><circle cx="11" cy="9" r="1" fill="#222"/></svg></span></div></article>
    <article class="product"><div class="product-name">GIRLS FANCY DRESS</div><div class="product-photo photo-white-dress" role="img" aria-label="Girl in a white layered party dress"></div><div class="buy"><span class="price">$50</span><span class="add">ADD TO CART<svg width="16" height="12" viewBox="0 0 14 10" aria-hidden="true"><path d="M0 1h3l2 6h7l1-4H4" fill="none" stroke="#222" stroke-width="1.3"/><circle cx="6" cy="9" r="1" fill="#222"/><circle cx="11" cy="9" r="1" fill="#222"/></svg></span></div></article>
    <article class="product"><div class="product-name">BOYS JACKET</div><div class="product-photo photo-jacket" role="img" aria-label="Four boys wearing jackets and jeans"></div><div class="buy"><span class="price">$50</span><span class="add">ADD TO CART<svg width="16" height="12" viewBox="0 0 14 10" aria-hidden="true"><path d="M0 1h3l2 6h7l1-4H4" fill="none" stroke="#222" stroke-width="1.3"/><circle cx="6" cy="9" r="1" fill="#222"/><circle cx="11" cy="9" r="1" fill="#222"/></svg></span></div></article>
    <article class="product"><div class="product-name">GIRLS FANCY DRESS</div><div class="product-photo photo-orange-dress" role="img" aria-label="Girl in an orange ruffled dress"></div><div class="buy"><span class="price">$50</span><span class="add">ADD TO CART<svg width="16" height="12" viewBox="0 0 14 10" aria-hidden="true"><path d="M0 1h3l2 6h7l1-4H4" fill="none" stroke="#222" stroke-width="1.3"/><circle cx="6" cy="9" r="1" fill="#222"/><circle cx="11" cy="9" r="1" fill="#222"/></svg></span></div></article>
  </div>
</section>

<section class="shelf" style="top:803px">
  <h2 class="shelf-title">Girls Dresses</h2>
  <div class="shelf-grid">
    <article class="product"><div class="product-name">NON IRON SHIRT FOR BOYS</div><div class="product-photo photo-shirt" role="img" aria-label="Blue short-sleeve boys shirt"></div><div class="buy"><span class="price">$50</span><span class="add">ADD TO CART<svg width="16" height="12" viewBox="0 0 14 10" aria-hidden="true"><path d="M0 1h3l2 6h7l1-4H4" fill="none" stroke="#222" stroke-width="1.3"/><circle cx="6" cy="9" r="1" fill="#222"/><circle cx="11" cy="9" r="1" fill="#222"/></svg></span></div></article>
    <article class="product"><div class="product-name">GIRLS FANCY DRESS</div><div class="product-photo photo-white-dress" role="img" aria-label="Girl in a white layered party dress"></div><div class="buy"><span class="price">$50</span><span class="add">ADD TO CART<svg width="16" height="12" viewBox="0 0 14 10" aria-hidden="true"><path d="M0 1h3l2 6h7l1-4H4" fill="none" stroke="#222" stroke-width="1.3"/><circle cx="6" cy="9" r="1" fill="#222"/><circle cx="11" cy="9" r="1" fill="#222"/></svg></span></div></article>
    <article class="product"><div class="product-name">BOYS JACKET</div><div class="product-photo photo-jacket" role="img" aria-label="Four boys wearing jackets and jeans"></div><div class="buy"><span class="price">$50</span><span class="add">ADD TO CART<svg width="16" height="12" viewBox="0 0 14 10" aria-hidden="true"><path d="M0 1h3l2 6h7l1-4H4" fill="none" stroke="#222" stroke-width="1.3"/><circle cx="6" cy="9" r="1" fill="#222"/><circle cx="11" cy="9" r="1" fill="#222"/></svg></span></div></article>
    <article class="product"><div class="product-name">GIRLS FANCY DRESS</div><div class="product-photo photo-orange-dress" role="img" aria-label="Girl in an orange ruffled dress"></div><div class="buy"><span class="price">$50</span><span class="add">ADD TO CART<svg width="16" height="12" viewBox="0 0 14 10" aria-hidden="true"><path d="M0 1h3l2 6h7l1-4H4" fill="none" stroke="#222" stroke-width="1.3"/><circle cx="6" cy="9" r="1" fill="#222"/><circle cx="11" cy="9" r="1" fill="#222"/></svg></span></div></article>
  </div>
</section>

<footer class="site-footer">
  <div class="footer-cols">
    <div><h3>Information</h3><ul><li>About us</li><li>Delivery Information</li><li>Privacy Policy</li><li>Terms &amp; Condition</li></ul></div>
    <div><h3>Our s upport</h3><ul><li>Delivery Information</li><li>Privacy Policy</li><li>Terms &amp; Condition</li><li>Contact Us</li></ul></div>
    <div><h3>Our service</h3><ul><li>My Account</li><li>Order History</li><li>Returns</li><li>Site Map</li></ul></div>
    <div><h3>Other more</h3><ul><li>Venenatis augue tellus</li><li>Proin mi lacus</li><li>Ornare vel lacus</li><li>Libero Sed rhoncus</li></ul></div>
  </div>
  <div class="footer-bottom">
    <div class="copyright"><span>ALL RIGHTS RESERVED</span><span>COPY RIGHT BRINDLE NETWORKS</span></div>
    <div class="pager"><i></i><i class="on"></i><i></i></div>
  </div>
</footer>

</body>
</html>
```